Bottle Label for New Brand of Boody Mary mix

We need a logo and label design for a new brand of bloody mary mix, the mix has Vodka premixed with all the spices and tomato juice, and all you add is the ice!
Currently under ingredient breakdown and government approval, looking to role out in a few months. Ideas for names are as follows, 'FULL KIT' or "DUSK ROVER" or 'Marigold' (like the bird, maybe Tawny Marigold) very open to all ideas, important to help consumer to remember the brand and understand is has everything included, all you need is ICE!

I have the owners of the mix reviewing the designs, will have feed back soon.

Thank you

```html
<!DOCTYPE html>
<html lang="en">
<head>
<meta charset="utf-8">
<title>Marigold Bloody Mary Label</title>
<link rel="stylesheet" href="https://fonts.googleapis.com/css2?family=Cinzel:wght@700;900&family=Uncial+Antiqua&family=Archivo:wght@700&display=swap">
<style>
  :root {
    --paper: #ffffff;
    --ray-light: #f4f4f4;
    --ray-mid: #dedede;
    --silver-dark: #3c3c3c;
    --silver-light: #d8d8d8;
    --emblem-red: #8e1418;
    --emblem-deep: #5a0a0d;
    --title-red: #e5432a;
    --crimson: #b3122c;
    --slate: #6e6e6e;
    --ink: #141414;
  }
  * { margin: 0; padding: 0; box-sizing: border-box; }
  html, body { width: 1200px; height: 1188px; overflow: hidden; background: var(--paper); }
  .label { position: relative; width: 1200px; height: 1188px; }
  .label-art { position: absolute; inset: 0; }
  .brand-name {
    font-family: "Cinzel", serif; font-weight: 900; font-size: 44px;
    letter-spacing: 6px; fill: var(--emblem-red);
  }
  .product-title {
    font-family: "Uncial Antiqua", serif; font-size: 60px;
    letter-spacing: 2px; fill: var(--title-red);
  }
  .product-type {
    font-family: "Archivo", sans-serif; font-weight: 700; font-size: 27px;
    letter-spacing: 2px; fill: var(--ink);
  }
  .banner-kicker {
    font-family: "Cinzel", serif; font-weight: 700; font-size: 52px;
    letter-spacing: 4px; fill: var(--slate);
  }
  .banner-call {
    font-family: "Cinzel", serif; font-weight: 900; font-size: 74px;
    letter-spacing: 3px; fill: var(--crimson);
  }
  .volume {
    font-family: "Archivo", sans-serif; font-weight: 700; font-size: 19px;
    letter-spacing: 1.5px; fill: var(--ink);
  }
</style>
</head>
<body>
<main class="label">
  <svg class="label-art" width="1200" height="1188" viewBox="0 0 1200 1188" xmlns="http://www.w3.org/2000/svg">
    <defs>
      <radialGradient id="label-field" cx="50%" cy="52%" r="60%">
        <stop offset="0" stop-color="var(--paper)"/>
        <stop offset="0.6" stop-color="var(--ray-light)"/>
        <stop offset="1" stop-color="var(--ray-mid)"/>
      </radialGradient>
      <linearGradient id="silver-frame" x1="0" y1="0" x2="1" y2="1">
        <stop offset="0" stop-color="var(--silver-dark)"/>
        <stop offset="0.35" stop-color="var(--silver-light)"/>
        <stop offset="0.7" stop-color="var(--silver-dark)"/>
        <stop offset="1" stop-color="var(--silver-light)"/>
      </linearGradient>
      <linearGradient id="banner-edge" x1="0" y1="0" x2="1" y2="0">
        <stop offset="0" stop-color="var(--ink)"/>
        <stop offset="0.5" stop-color="#555"/>
        <stop offset="1" stop-color="var(--ink)"/>
      </linearGradient>
      <radialGradient id="emblem-fill" cx="45%" cy="40%" r="60%">
        <stop offset="0" stop-color="var(--emblem-red)"/>
        <stop offset="1" stop-color="var(--emblem-deep)"/>
      </radialGradient>
    </defs>

    <!-- label body -->
    <path class="label-body" d="M352 262 H848 Q850 292 880 294 V1078 H320 V294 Q350 292 352 262 Z"
          fill="url(#label-field)" stroke="url(#silver-frame)" stroke-width="12"
          role="img" aria-label="Silver sunburst rays radiating from the label centre"/>

    <!-- brand mark area -->
    <circle class="brand-dot" cx="600" cy="165" r="150" fill="url(#emblem-fill)"/>
    <text class="brand-name" x="600" y="378" text-anchor="middle">MARIGOLD</text>

    <!-- product title -->
    <text class="product-title" x="600" y="560" text-anchor="middle">BLOODY MARY</text>
    <text class="product-type" x="600" y="596" text-anchor="middle">VODKA PREMIXED</text>

    <!-- tilted banner -->
    <g class="banner" transform="rotate(-8 600 725)">
      <rect x="262" y="625" width="676" height="200" fill="url(#banner-edge)"/>
      <rect x="278" y="641" width="644" height="168" fill="var(--paper)"/>
      <text class="banner-kicker" x="600" y="712" text-anchor="middle">FULL KIT.</text>
      <text class="banner-call" x="600" y="790" text-anchor="middle">JUST ADD ICE!</text>
    </g>

    <!-- volume -->
    <text class="volume" x="600" y="978" text-anchor="middle">33.8 FL. OZ. / 1 LITER</text>
  </svg>
</main>
</body>
</html>
```